Card Design for my dog training business Rustpaw Obedience

Need a business card design for my dog training business with my new logo. Want the card to come off professional yet fun. Want it to be very eye catchy as well. I normally have these at vet clinics, pet stores, and groomers. so need it to look better than my competitors.
Target Market(s)
dog owners
Industry/Entity Type
Dog Training
Contact Information for Business Card
needs logo, my name and info
Font styles to use
Serif
Colors
0255a3
ffffff
ec1f27
000000
333333
fbfbfb
Requirements
Must have
- Rustpaw Obedience
- Hollis Brandt
- 415 903 2267
- info@rustpawobedience.example
- www.rustpawobedience.example

```html
<!DOCTYPE html>
<html lang="en">
<head>
<meta charset="utf-8">
<title>Rustpaw Obedience — Business Card</title>
<link rel="stylesheet" href="https://fonts.googleapis.com/css2?family=Libre+Baskerville:ital,wght@0,400;1,400&family=Montserrat:wght@400;700&display=swap">
<style>
  :root {
    --brand-blue: #0255a3;
    --brand-red: #ec1f27;
    --white: #ffffff;
    --ink: #000000;
    --ink-soft: #333333;
    --paper: #fbfbfb;
    --backdrop: #ececec;
  }
  * { box-sizing: border-box; margin: 0; padding: 0; }
  html, body {
    width: 1200px; height: 1200px; overflow: hidden;
    background: var(--backdrop);
  }
  .sheet {
    width: 1200px; height: 1200px;
    display: flex; flex-direction: column; align-items: center; justify-content: center;
    gap: 60px;
  }
  .card {
    position: relative;
    width: 900px; height: 514px;
    overflow: hidden;
    box-shadow: 0 6px 18px rgba(0,0,0,0.12);
  }

  /* Front */
  .card-front { background: var(--brand-blue); }
  .front-logo {
    position: absolute; left: 0; right: 0; top: 150px;
    text-align: center;
    font-family: "Libre Baskerville", serif;
    font-size: 46px; letter-spacing: 1px;
    color: var(--white);
  }
  .tagline-band {
    position: absolute; left: 0; right: 0; bottom: 62px;
    height: 46px;
    background: var(--brand-red);
    display: flex; align-items: center; justify-content: flex-end;
    padding-right: 170px;
  }
  .tagline {
    font-family: "Libre Baskerville", serif;
    font-style: italic;
    font-size: 19px;
    color: var(--white);
    white-space: nowrap;
  }

  /* Back */
  .card-back { background: var(--paper); }
  .back-logo {
    position: absolute; right: 90px; top: 120px;
    display: flex; align-items: center; gap: 14px;
    font-family: "Libre Baskerville", serif;
    font-size: 38px;
    color: var(--brand-blue);
    white-space: nowrap;
  }
  .back-logo .mark {
    width: 22px; height: 22px; background: var(--brand-red);
  }
  .holder {
    position: absolute; left: 70px; top: 250px;
    font-family: "Montserrat", sans-serif;
  }
  .holder-name {
    font-size: 28px; font-weight: 700; color: var(--brand-blue);
  }
  .holder-role {
    font-size: 18px; color: var(--ink-soft); margin-top: 4px;
  }
  .divider {
    width: 28px; height: 3px; background: var(--ink);
    margin: 30px 0 32px 28px;
  }
  .contact-list { list-style: none; margin-left: 30px; }
  .contact-list li {
    display: flex; align-items: center; gap: 12px;
    font-size: 18px; color: var(--ink); line-height: 1.55;
    white-space: nowrap;
  }
  .contact-list svg { width: 16px; height: 16px; flex: none; }
</style>
</head>
<body>
  <main class="sheet">
    <section class="card card-front" aria-label="Card front">
      <div class="front-logo">Rustpaw Obedience</div>
      <div class="tagline-band">
        <p class="tagline">“Building better manners one lesson at a time.”</p>
      </div>
    </section>

    <section class="card card-back" aria-label="Card back">
      <div class="back-logo"><span class="mark"></span>Rustpaw Obedience</div>
      <div class="holder">
        <h1 class="holder-name">Hollis Brandt</h1>
        <p class="holder-role">Owner</p>
        <div class="divider"></div>
        <ul class="contact-list">
          <li>
            <svg viewBox="0 0 16 16" aria-hidden="true"><path d="M3.5 1.5l3 3-1.6 1.8c.8 1.8 2.2 3.2 4 4l1.8-1.6 3 3-2 2C6.5 13.5 2.5 9.5 1.5 3.5z" fill="var(--brand-red)"/></svg>
            415 903 2267
          </li>
          <li>
            <svg viewBox="0 0 16 16" aria-hidden="true"><rect x="1.5" y="3.5" width="13" height="9" fill="none" stroke="var(--brand-red)" stroke-width="1.6"/><path d="M1.5 3.5l6.5 5 6.5-5" fill="none" stroke="var(--brand-red)" stroke-width="1.6"/></svg>
            info@rustpawobedience.example
          </li>
          <li>
            <svg viewBox="0 0 16 16" aria-hidden="true"><circle cx="8" cy="8" r="6.5" fill="none" stroke="var(--brand-red)" stroke-width="1.5"/><ellipse cx="8" cy="8" rx="2.8" ry="6.5" fill="none" stroke="var(--brand-red)" stroke-width="1.2"/><path d="M1.5 8h13" stroke="var(--brand-red)" stroke-width="1.2"/></svg>
            www.rustpawobedience.example
          </li>
        </ul>
      </div>
    </section>
  </main>
</body>
</html>
```